Business Card Design For a Medical Device Supplier for Orthopaedics
BayRidge Joint Advisors Inc.
Business Card Design For a Medical Device Supplier for Orthopaedics - Medical
Creative Brief
Professional
Tom Lusker
Principle
415 Wren Hollow Ct. Larkhaven, CA 94599
tomlusker@bayridgejoint.org
www.bayridgejoint.org
I am looking for the logo to be part of the entire card in ghost format. HAve my name and contact info on the front
HAve BJA Stamp on the back and list my Companies I represent Kinderlimbix Vantrel Drive Lumoray Medical Equiptment

```html
<!DOCTYPE html>
<html lang="en">
<head>
<meta charset="utf-8">
<title>BayRidge Joint Advisors Inc. — Business Card</title>
<link href="https://fonts.googleapis.com/css2?family=Open+Sans:wght@400;600;700&display=swap" rel="stylesheet">
<style>
  :root {
    --bg: #e9ecee;
    --card: #ffffff;
    --teal: #2f7f9c;
    --teal-light: #7fb2c6;
    --ink: #ffffff;
    --grey: #8a9aa3;
    --text-dark: #4d6470;
    --shadow: rgba(30, 50, 60, 0.18);
  }
  * { margin: 0; padding: 0; box-sizing: border-box; }
  html, body {
    width: 1200px; height: 838px; overflow: hidden;
    background: var(--bg);
    font-family: "Open Sans", Arial, sans-serif;
  }
  .sheet {
    width: 1200px; height: 838px;
    display: flex; align-items: center; justify-content: center; gap: 40px;
  }
  .card {
    position: relative;
    width: 550px; height: 314px;
    background: var(--card);
    box-shadow: 0 10px 30px var(--shadow);
    overflow: hidden;
  }

  /* Front */
  .front-brand {
    position: absolute; top: 56px; left: 0; right: 0;
    display: flex; align-items: center; justify-content: center; gap: 12px;
  }
  .brand-dot {
    width: 26px; height: 26px; border-radius: 50%;
    background: var(--teal);
  }
  .brand-name {
    font-weight: 600; font-size: 25px; color: var(--teal);
    letter-spacing: 0.5px;
  }
  .front-band {
    position: absolute; left: 0; right: 0; bottom: 0; height: 128px;
    background: var(--teal);
    border-top: 5px solid var(--teal-light);
    color: var(--ink);
    display: flex; justify-content: space-between;
    padding: 20px 34px 0 42px;
  }
  .person-name { font-weight: 700; font-size: 18px; }
  .person-title { font-size: 12px; margin: 1px 0 8px 70px; }
  .address { font-size: 12px; line-height: 1.45; }
  .contact-list { list-style: none; font-size: 12px; line-height: 1.6; padding-top: 4px; }
  .contact-list li { display: flex; align-items: center; gap: 7px; }
  .contact-list svg { width: 11px; height: 11px; fill: none; stroke: var(--ink); stroke-width: 1.6; }

  /* Back */
  .back-stamp {
    position: absolute; left: 70px; top: 92px;
    width: 130px; height: 130px; border-radius: 50%;
    border: 4px solid var(--grey);
    display: flex; align-items: center; justify-content: center;
  }
  .stamp-name { font-weight: 600; font-size: 30px; color: var(--grey); }
  .companies {
    position: absolute; left: 280px; top: 82px;
    color: var(--teal);
  }
  .companies-title { font-size: 20px; font-weight: 600; margin-bottom: 16px; }
  .companies-list { list-style: none; font-size: 14px; line-height: 2; color: var(--text-dark); }
  .companies-list li::before {
    content: ""; display: inline-block; width: 5px; height: 5px;
    border-radius: 50%; background: var(--teal); margin-right: 10px; vertical-align: middle;
  }
</style>
</head>
<body>
<main class="sheet">

  <section class="card card-front" aria-label="Card front">
    <div class="front-brand">
      <span class="brand-dot"></span>
      <span class="brand-name">BayRidge Joint Advisors Inc.</span>
    </div>
    <div class="front-band">
      <div class="person">
        <p class="person-name">Tom Lusker</p>
        <p class="person-title">Principle</p>
        <p class="address">415 Wren Hollow Ct.<br>Larkhaven, CA 94599</p>
      </div>
      <ul class="contact-list">
        <li><svg viewBox="0 0 12 12"><rect x="3" y="1" width="6" height="10" rx="1"/></svg>925-555-0142</li>
        <li><svg viewBox="0 0 12 12"><path d="M3 1 L5 3 L4 5 Q6 8 7 8 L9 7 L11 9 L9 11 Q2 9 1 3 Z"/></svg>925-555-0187</li>
        <li><svg viewBox="0 0 12 12"><rect x="1" y="3" width="10" height="7"/><path d="M1 3 L6 7 L11 3"/></svg>tomlusker@bayridgejoint.org</li>
        <li><svg viewBox="0 0 12 12"><circle cx="6" cy="6" r="5"/><path d="M1 6 H11 M6 1 Q3 6 6 11 M6 1 Q9 6 6 11"/></svg>www.bayridgejoint.org</li>
      </ul>
    </div>
  </section>

  <section class="card card-back" aria-label="Card back">
    <div class="back-stamp"><span class="stamp-name">BJA</span></div>
    <div class="companies">
      <h2 class="companies-title">Our Companies</h2>
      <ul class="companies-list">
        <li>Kinderlimbix</li>
        <li>Vantrel Drive</li>
        <li>Lumoray Medical Equiptment</li>
      </ul>
    </div>
  </section>

</main>
</body>
</html>
```